VelmoraTrade.com -Ecommerce Website for Luxury Products

This will be an ecommerce site. A website portal that will allow both consumers to enter one way and see specific purchase options and businesses to enter via a different link that allows B2B to see their specific options once logged into. B2C can purchase both as a guest/or after account is setup. B2B must be approved to set up account. This is front end website project. Back-end integration is separate. Will be hosted on Serventa with a domain registration held at PortaVance. Additional website concept/idea/synergy can be found from sister site-KRWEHospitality.com

```html
<!DOCTYPE html>
<html lang="en">
<head>
<meta charset="utf-8">
<title>VelmoraTrade — Purveyors of Luxury Lifestyle Accoutrements</title>
<link rel="stylesheet" href="https://fonts.googleapis.com/css2?family=Cinzel:wght@500;600&family=Playfair+Display:wght@500;600;700&family=Montserrat:wght@400;500;600&display=swap">
<style>
  :root {
    --ink: #141414;
    --night: #1b1b1b;
    --night-deep: #0d0b08;
    --gold: #c9a66b;
    --gold-bright: #e0bd7a;
    --cream: #f4f1ea;
    --paper: #ffffff;
    --text: #2a2a2a;
    --muted: #6f6a62;
    --on-dark: #e9e4da;
    --frame: #a08b70;
  }
  * { box-sizing: border-box; margin: 0; padding: 0; }
  html, body { width: 1200px; height: 2212px; overflow: hidden; }
  body {
    background: var(--frame);
    font-family: "Montserrat", Arial, sans-serif;
    color: var(--text);
  }
  .page { width: 1200px; height: 2212px; position: relative; }
  section, header, footer { overflow: hidden; }

  /* Hero */
  .hero { position: relative; height: 760px; color: var(--on-dark); text-align: center; }
  .hero-backdrop {
    position: absolute; inset: 0;
    background:
      radial-gradient(ellipse 420px 260px at 72% 30%, rgba(224,189,122,.55), transparent 70%),
      radial-gradient(ellipse 520px 220px at 35% 55%, rgba(201,166,107,.35), transparent 70%),
      radial-gradient(ellipse 300px 160px at 15% 20%, rgba(201,166,107,.25), transparent 70%),
      linear-gradient(180deg, #1a140c 0%, var(--night-deep) 60%, #16110a 100%);
  }
  .site-nav { position: relative; display: flex; justify-content: center; gap: 34px; padding-top: 24px; }
  .site-nav a { color: var(--on-dark); text-decoration: none; font-size: 12px; letter-spacing: 1.5px; font-weight: 500; }
  .hero-content { position: relative; padding-top: 170px; }
  .brand-mark { display: inline-flex; align-items: center; gap: 18px; }
  .brand-dot { width: 16px; height: 16px; border-radius: 50%; background: var(--gold); }
  .brand-name { font-family: "Cinzel", serif; font-weight: 500; font-size: 74px; letter-spacing: 3px; color: #f2ede2; line-height: 1; }
  .brand-division { font-family: "Cinzel", serif; font-size: 26px; letter-spacing: 3px; margin-top: 12px; color: #f2ede2; }
  .hero-title { font-family: "Playfair Display", serif; font-weight: 500; font-size: 34px; color: var(--gold-bright); margin-top: 36px; }
  .hero-tagline { font-size: 15px; margin-top: 26px; color: var(--on-dark); }
  .hero-actions { display: flex; justify-content: center; gap: 22px; margin-top: 34px; }
  .btn { display: inline-block; font-size: 12px; letter-spacing: 1px; font-weight: 600; line-height: 14px; padding: 12px 22px; text-decoration: none; text-transform: uppercase; }
  .btn-gold { background: var(--gold); color: var(--ink); }
  .btn-outline { border: 1px solid var(--gold); color: var(--gold); }
  .btn-outline-light { border: 1px solid var(--on-dark); color: var(--on-dark); }

  .section-title { font-family: "Playfair Display", serif; font-weight: 700; font-size: 30px; line-height: 40px; color: var(--ink); text-align: center; }
  .section-rule { width: 46px; height: 2px; background: var(--gold); margin: 12px auto 0; }

  /* Collections */
  .collections { height: 320px; background: var(--cream); padding-top: 54px; text-align: center; }
  .collection-grid { display: flex; justify-content: center; gap: 22px; margin-top: 26px; }
  .collection-card { width: 205px; height: 96px; padding: 14px 14px; text-align: center; }
  .collection-card h3 { font-family: "Playfair Display", serif; font-size: 16px; line-height: 20px; font-weight: 600; color: var(--ink); }
  .collection-card p { font-size: 10.5px; line-height: 1.5; color: var(--muted); margin-top: 8px; }
  .collection-card.is-featured { background: var(--paper); box-shadow: 0 6px 18px rgba(0,0,0,.12); }
  .collections .btn { margin-top: 20px; padding: 10px 20px; }

  /* About */
  .about { height: 300px; background: var(--paper); padding-top: 52px; text-align: center; }
  .about-text { width: 740px; margin: 20px auto 0; font-size: 12px; line-height: 20px; color: var(--muted); }
  .about .btn { margin-top: 24px; padding: 8px 18px; font-size: 10px; }

  /* Partner */
  .partner { height: 290px; background: var(--night); padding-top: 62px; text-align: center; color: var(--on-dark); }
  .partner .section-title { color: #f2ede2; }
  .partner-text { width: 620px; margin: 20px auto 0; font-size: 12.5px; line-height: 21px; }
  .partner .btn { margin-top: 24px; font-size: 10px; padding: 9px 18px; }

  /* Showcase */
  .showcase { height: 250px; background: var(--cream); padding-top: 80px; text-align: center; }
  .showcase-list { display: flex; justify-content: space-between; width: 820px; margin: 30px auto 0; list-style: none; font-size: 14px; color: var(--text); }

  /* Footer */
  .site-footer { height: 292px; background: var(--ink); color: var(--on-dark); position: relative; padding: 40px 0 0 190px; }
  .footer-cols { display: flex; }
  .footer-col h4 { font-family: "Playfair Display", serif; font-size: 15px; font-weight: 600; color: #f2ede2; margin-bottom: 12px; }
  .footer-col ul { list-style: none; font-size: 12px; line-height: 1.9; }
  .footer-col.nav-col { width: 330px; }
  .footer-col.contact-col { width: 430px; }
  .footer-legal { position: absolute; left: 0; right: 0; bottom: 18px; text-align: center; font-size: 10px; color: #8f8a80; border-top: 1px solid #2e2e2e; padding-top: 12px; margin: 0 190px; }
</style>
</head>
<body>
<div class="page">

  <header class="hero">
    <div class="hero-backdrop" role="img" aria-label="Dark background with sweeping golden light trails and glowing sparkles"></div>
    <nav class="site-nav">
      <a href="#">HOME</a><a href="#">ABOUT</a><a href="#">COLLECTIONS</a><a href="#">WHOLESALE</a><a href="#">PARTNERS</a><a href="#">CONTACT</a>
    </nav>
    <div class="hero-content">
      <div class="brand-mark"><span class="brand-dot"></span><span class="brand-name">VELMORATRADE</span></div>
      <div class="brand-division">A DIVISION OF KRWE HOSPITALITY</div>
      <h1 class="hero-title">Purveyors of Luxury Lifestyle Accoutrements</h1>
      <p class="hero-tagline">Curating limited edition luxury items that are one of a kind &amp; iconic.</p>
      <div class="hero-actions">
        <a class="btn btn-gold" href="#">Shop Now</a>
        <a class="btn btn-outline-light" href="#">Wholesale Login</a>
      </div>
    </div>
  </header>

  <section class="collections">
    <h2 class="section-title">Our Collections</h2>
    <div class="section-rule"></div>
    <div class="collection-grid">
      <article class="collection-card"><h3>Cigar Accessories</h3><p>Premium humidors, cutters, lighters and curated cigar essentials.</p></article>
      <article class="collection-card is-featured"><h3>Oils &amp; Fragrances</h3><p>Intoxicating oils and fragrances crafted for the discerning palate.</p></article>
      <article class="collection-card"><h3>Attire &amp; Accessories</h3><p>Luxury clothing, travel goods and accessories to elevate your style.</p></article>
      <article class="collection-card"><h3>Limited Editions</h3><p>Exclusive releases and one-of-a-kind pieces for true connoisseurs.</p></article>
    </div>
    <a class="btn btn-outline" href="#">Explore All</a>
  </section>

  <section class="about">
    <h2 class="section-title">About VelmoraTrade</h2>
    <p class="about-text">Elegant, confident and refined, VelmoraTrade speaks to both the discerning consumer and the sophisticated business owner. Our carefully selected pieces honour exclusivity, craftsmanship and personal indulgence, while our wholesale program empowers partners with curated, quality goods and brand elevation. As a division of KRWE Hospitality, we curate world-class offerings that elevate everyday experiences.</p>
    <a class="btn btn-outline" href="#">Learn More</a>
  </section>

  <section class="partner">
    <h2 class="section-title">Become a Partner</h2>
    <p class="partner-text">Elevate your lounge and impress your clientele with our curated selection of luxury lifestyle accoutrements. Register for our wholesale portal to access exclusive collections, partner pricing and dedicated support.</p>
    <a class="btn btn-gold" href="#">Register for Wholesale</a>
  </section>

  <section class="showcase">
    <h2 class="section-title">Partner Showcase</h2>
    <ul class="showcase-list">
      <li>Lounge A</li><li>Club B</li><li>Resort C</li><li>Bar D</li>
    </ul>
  </section>

  <footer class="site-footer">
    <div class="footer-cols">
      <div class="footer-col nav-col">
        <h4>Navigate</h4>
        <ul><li>Home</li><li>About</li><li>Collections</li><li>Wholesale</li><li>Partners</li><li>Contact</li></ul>
      </div>
      <div class="footer-col contact-col">
        <h4>Contact</h4>
        <ul><li>Email: info@velmoratrade.com</li><li>Phone: +1 (555) 014-2287</li><li>Location: Global Headquarters</li></ul>
      </div>
      <div class="footer-col">
        <h4>Follow Us</h4>
      </div>
    </div>
    <p class="footer-legal">© 2024 VelmoraTrade. All rights reserved.</p>
  </footer>

</div>
</body>
</html>
```